Design some Business Cards, stationery and a Powerpoint slide template for qorvix Pty Ltd

Hi,

qorvix Pty Ltd is a new and very ambitious Internet technology startup. Since we're busy getting the technology under control to grow we'd need some help with getting some of our branding materials ready :-) We had a great logo created a few weeks ago and now need a business card template, a letterhead/stationery template and an MS Powerpoint slide template that include the logo and the design of which goes nicely with the domain we are active in.

We'd like to invite you to join the competition and submit your proposal.

We're active in the broader domains of:
- Internet Technology
- Distributed Computing
- Crowd sourcing
- Sustainability
- Supercomputing
- Hive Computing
- Superscale computing

************************
The business card template should include:

logo (see attached .png),
business name (qorvix Pty Ltd),
placeholders for: business address (2 lines), name of staff member, position of staff member, phone number, email, website URL, facebook URL
***********************
The stationery template should include:

logo
business name
placeholders for: business address (at top of page), company phone number and email address (at top of page), bank details (at bottom of page), company registration details (at bottom of page)
***********************
The Powerpoint slide template should include:

logo
business name
speaker name & email address
**********************

Some samples of the kinds of designs we're after -
http://lumbertide-gallery.example/branding/plover-atelier-identity/ (though the colours would be similar to those in our logo, not the yellow of this sample),
http://lumbertide-gallery.example/branding/tovelin/,
http://lumbertide-gallery.example/branding/rendo/

Thanks for your help!

```html
<!DOCTYPE html>
<html lang="en">
<head>
<meta charset="utf-8">
<title>qorvix Pty Ltd – Stationery Set</title>
<link rel="stylesheet" href="https://fonts.googleapis.com/css2?family=Open+Sans:wght@400;600;700&family=EB+Garamond:wght@400;500;600&display=swap">
<style>
:root{
  --backdrop:#2c2c2c;
  --paper:#ffffff;
  --paper-soft:#eef0ee;
  --slate:#3e4b50;
  --slate-dark:#334045;
  --green:#5b9b3b;
  --green-light:#8cbf5e;
  --ink:#333a3d;
  --muted:#7b8588;
  --mark-faint:#e3e7e3;
}
*{margin:0;padding:0;box-sizing:border-box}
html,body{width:1200px;height:847px;overflow:hidden;background:var(--backdrop)}
body{position:relative;font-family:"Open Sans",Arial,sans-serif;color:var(--ink)}
.piece{position:absolute;background:var(--paper);overflow:hidden}
.wordmark{display:flex;align-items:center;gap:5px;font-family:"Open Sans",Arial,sans-serif;font-weight:600;color:var(--slate)}
.wordmark .dot{border-radius:50%;background:var(--green);flex:none}
.swoosh{position:absolute;left:0;bottom:0;width:100%}
.faint-mark{position:absolute;border-radius:50%;background:radial-gradient(circle,var(--mark-faint) 0%,rgba(227,231,227,0) 70%)}

/* Letterhead */
.letterhead{left:80px;top:112px;width:443px;height:620px}
.letterhead .wordmark{position:absolute;left:130px;top:30px;font-size:26px}
.letterhead .wordmark .dot{width:22px;height:22px}
.letterhead .contact{position:absolute;left:292px;top:30px;font-size:5.5px;line-height:8px;color:var(--muted);border-left:1px solid #ccc;padding-left:6px}
.letterhead .contact strong{color:var(--ink);font-size:6px}
.letterhead .faint-mark{left:110px;top:300px;width:300px;height:300px}
.letter{position:absolute;left:30px;top:100px;width:385px;font-size:7.6px;line-height:9.6px;color:var(--ink)}
.letter p{margin-bottom:9px}
.letter .subject{text-transform:uppercase}
.letter .sign{font-family:"EB Garamond",serif;font-style:italic;font-size:12px;border-bottom:1px solid #555;width:62px;margin:2px 0 2px}
.letterhead .bank{position:absolute;left:10px;bottom:8px;font-size:6px;line-height:8px;color:#fff;font-weight:600}

/* Business cards */
.card-front{left:572px;top:45px;width:248px;height:139px}
.card-front .wordmark{position:absolute;left:14px;top:30px;font-size:22px}
.card-front .wordmark .dot{width:20px;height:20px}
.card-front .person{position:absolute;right:8px;top:6px;text-align:right;font-size:6px;line-height:7px;color:var(--muted)}
.card-front .person strong{color:var(--green);font-size:6.5px}
.card-front .lines{position:absolute;left:20px;top:60px;font-size:5px;line-height:7.2px;color:var(--muted)}
.card-front .lines strong{color:var(--ink)}
.card-front .web{position:absolute;right:10px;bottom:6px;font-size:5.5px;color:#fff}
.card-back{left:572px;top:205px;width:248px;height:160px;background:var(--slate)}
.card-back .wordmark{position:absolute;left:14px;top:64px;font-size:24px;color:#fff}
.card-back .wordmark .dot{width:20px;height:20px}
.card-back .faint-mark{left:110px;top:-10px;width:160px;height:160px;background:radial-gradient(circle,rgba(255,255,255,.10) 0%,rgba(255,255,255,0) 68%)}

/* Envelope */
.env-front{left:841px;top:45px;width:359px;height:153px}
.env-front .wordmark{position:absolute;left:22px;top:14px;font-size:17px}
.env-front .wordmark .dot{width:15px;height:15px}
.env-front .addr{position:absolute;left:26px;top:106px;font-size:4.5px;line-height:6px;color:var(--muted)}
.env-front .faint-mark{left:200px;top:0;width:140px;height:140px}
.env-back{left:841px;top:209px;width:359px;height:156px}
.env-back svg{position:absolute;inset:0}
.env-back .web{position:absolute;left:0;right:0;top:12px;text-align:center;font-size:5px;color:#fff}

/* Slides */
.slide{width:289px;height:215px;background:linear-gradient(180deg,#fafbfa 0%,var(--paper-soft) 100%)}
.slide .wordmark{position:absolute;left:10px;top:8px;font-size:14px}
.slide .wordmark .dot{width:12px;height:12px}
.slide .faint-mark{left:130px;top:40px;width:170px;height:170px}
.slide .footer{position:absolute;left:24px;bottom:9px;font-size:4.5px;color:#fff}
.slide-title{left:572px;top:396px}
.slide-title h2{position:absolute;left:18px;top:92px;font-family:"EB Garamond",serif;font-weight:500;font-size:21px;color:var(--green)}
.slide-title h3{position:absolute;left:18px;top:116px;font-family:"EB Garamond",serif;font-weight:600;font-size:13px;color:var(--slate)}
.slide-thanks{left:886px;top:396px}
.slide-thanks h2{position:absolute;left:18px;top:86px;font-family:"EB Garamond",serif;font-weight:600;font-size:30px;color:var(--green)}
.slide-content{left:572px;top:628px;height:213px;background:var(--paper)}
.slide-content h2{position:absolute;right:18px;top:22px;font-family:"EB Garamond",serif;font-weight:500;font-size:16px;color:var(--green)}
.slide-content .body{position:absolute;left:20px;top:44px;width:245px;font-family:"EB Garamond",serif;font-size:7.6px;line-height:9px;color:var(--ink)}
.slide-content .body p{margin-bottom:6px}
</style>
</head>
<body>

<!-- Letterhead -->
<section class="piece letterhead">
  <div class="wordmark"><span class="dot"></span>qorvix</div>
  <div class="contact"><strong>qorvix Pty Ltd</strong><br>PO Box 456, Alton 5678<br>Harbourview, Australia<br>+61(3) 5550 0142<br>info@qorvix.example<br>www.qorvix.example</div>
  <div class="faint-mark" role="img" aria-label="Faint brand mark watermark"></div>
  <div class="letter">
    <p>Ref. No. : ABC/500/SP/06<br>Dated :&nbsp;&nbsp;&nbsp;&nbsp;&nbsp;&nbsp;&nbsp;24 April, 2013</p>
    <p>Mr. Martin Ellery<br>Director, Sales and Marketing<br>Harwick Biolabs Group of Companies Limited<br>House – 48/C, Road – 7 (New), Brookfield Park, Dunmere</p>
    <p class="subject">Proposal for work with you as your communication partner</p>
    <p>With due respect, would like to take the opportunity for proposing ourselves as your communication partner. With a view to introduce ourselves would like to mention that we - the Norvale Collective, have stepped into operation recently but having a team of expertise for a long. We are confident to assure the best possible services with highest dedication round the clock.</p>
    <p>Now-a-days Advertisement has become a Communication Technology that employed in transmitting messages –<br>• the art and technique of using words effectively to impart information or ideas;<br>• the field of study concerned with the transmission of information by various means, such as print or broadcasting or direct;<br>•the exchange of thoughts, messages, or information, as by speech, signals, writing, action or behavior.</p>
    <p>We understand that technology is blending with this sector and we are able to keep pace with the continuous changing of this. Thereby, we remain ready to strategize our clients in views of the then market development and dynamics.</p>
    <p>Looking forward a strong and fruitful business relationship in the days to come.</p>
    <p style="margin-bottom:0">Regards</p>
    <div class="sign">R. T. Selwyn</div>
    <p>R. T. Selwyn<br>Chief Designer</p>
  </div>
  <svg class="swoosh" width="443" height="80" viewBox="0 0 443 80" preserveAspectRatio="none" aria-hidden="true">
    <path d="M0 46 Q220 70 443 8 L443 80 L0 80Z" fill="var(--green)"/>
    <path d="M0 52 Q220 76 443 20 L443 80 L0 80Z" fill="var(--slate)"/>
  </svg>
  <div class="bank">Bank details: Halden Mutual Bank,<br>Box 2290, 4410 Account No: 55-204.318-00<br>Registration Number: 0000000000</div>
</section>

<!-- Business card front -->
<section class="piece card-front">
  <div class="person"><strong>LENA MARSH</strong><br>Chairman</div>
  <div class="wordmark"><span class="dot"></span>qorvix</div>
  <div class="lines"><strong>qorvix Pty Ltd</strong><br>PO Box 456, Alton 5678<br>Harbourview, Australia<br>+61(3) 5550 0142<br>info@qorvix.example<br>social.example/qorvix</div>
  <svg class="swoosh" width="248" height="34" viewBox="0 0 248 34" preserveAspectRatio="none" aria-hidden="true">
    <path d="M0 16 Q120 30 248 2 L248 34 L0 34Z" fill="var(--green)"/>
    <path d="M0 22 Q120 34 248 12 L248 34 L0 34Z" fill="var(--slate)"/>
  </svg>
  <div class="web">www.qorvix.example</div>
</section>

<!-- Business card back -->
<section class="piece card-back">
  <div class="faint-mark" role="img" aria-label="Faint brand mark watermark"></div>
  <div class="wordmark"><span class="dot"></span>qorvix</div>
</section>

<!-- Envelope front -->
<section class="piece env-front">
  <div class="faint-mark" role="img" aria-label="Faint brand mark watermark"></div>
  <div class="wordmark"><span class="dot"></span>qorvix</div>
  <div class="addr">qorvix Pty Ltd<br>PO Box 456, Alton 5678, Harbourview<br>+61(3) 5550 0142 · info@qorvix.example</div>
  <svg class="swoosh" width="359" height="40" viewBox="0 0 359 40" preserveAspectRatio="none" aria-hidden="true">
    <path d="M0 30 Q180 36 359 0 L359 40 L0 40Z" fill="var(--green)"/>
    <path d="M0 34 Q180 40 359 10 L359 40 L0 40Z" fill="#dde2e3"/>
  </svg>
</section>

<!-- Envelope back -->
<section class="piece env-back">
  <svg width="359" height="156" viewBox="0 0 359 156" aria-hidden="true">
    <line x1="0" y1="156" x2="150" y2="70" stroke="#c9cdce" stroke-width="0.8"/>
    <line x1="359" y1="156" x2="209" y2="70" stroke="#c9cdce" stroke-width="0.8"/>
    <path d="M0 0 L359 0 L359 20 Q180 70 0 20Z" fill="var(--slate)"/>
    <path d="M0 20 Q180 70 359 20" fill="none" stroke="var(--green)" stroke-width="1.5"/>
  </svg>
  <div class="web">www.qorvix.example</div>
</section>

<!-- Title slide -->
<section class="piece slide slide-title">
  <div class="faint-mark" role="img" aria-label="Faint brand mark watermark"></div>
  <div class="wordmark"><span class="dot"></span>qorvix</div>
  <h2>Click to add title</h2>
  <h3>Click to add subtitle</h3>
  <svg class="swoosh" width="289" height="40" viewBox="0 0 289 40" preserveAspectRatio="none" aria-hidden="true">
    <path d="M0 20 Q140 34 289 0 L289 40 L0 40Z" fill="var(--green)"/>
    <path d="M0 24 Q140 38 289 8 L289 40 L0 40Z" fill="var(--slate)"/>
  </svg>
  <div class="footer">Lena Marsh &nbsp;|&nbsp; lena@qorvix.example</div>
</section>

<!-- Closing slide -->
<section class="piece slide slide-thanks">
  <div class="faint-mark" role="img" aria-label="Faint brand mark watermark"></div>
  <div class="wordmark"><span class="dot"></span>qorvix</div>
  <h2>Thank You</h2>
  <svg class="swoosh" width="289" height="40" viewBox="0 0 289 40" preserveAspectRatio="none" aria-hidden="true">
    <path d="M0 20 Q140 34 289 0 L289 40 L0 40Z" fill="var(--green)"/>
    <path d="M0 24 Q140 38 289 8 L289 40 L0 40Z" fill="var(--slate)"/>
  </svg>
  <div class="footer">Lena Marsh &nbsp;|&nbsp; lena@qorvix.example</div>
</section>

<!-- Content slide -->
<section class="piece slide slide-content">
  <div class="faint-mark" role="img" aria-label="Faint brand mark watermark"></div>
  <div class="wordmark"><span class="dot"></span>qorvix</div>
  <h2>Click to add title</h2>
  <div class="body">
    <p>With due respect, would like to take the opportunity for proposing ourselves as your communication partner. With a view to introduce ourselves would like to mention that we – the Norvale Collective, have stepped into operation recently but having a team of expertise for a long. We are confident to assure the best possible services with highest dedication round the clock.</p>
    <p>• the art and technique of using words effectively to impart information or ideas;<br>• the field of study concerned with the transmission of information by various means, such as print or broadcasting or direct;<br>•the exchange of thoughts, messages, or information, as by speech, signals, writing, action or behavior.</p>
  </div>
  <svg class="swoosh" width="289" height="36" viewBox="0 0 289 36" preserveAspectRatio="none" aria-hidden="true">
    <path d="M0 18 Q140 30 289 0 L289 36 L0 36Z" fill="var(--green)"/>
    <path d="M0 22 Q140 34 289 8 L289 36 L0 36Z" fill="var(--slate)"/>
  </svg>
  <div class="footer">Lena Marsh &nbsp;|&nbsp; lena@qorvix.example</div>
</section>

</body>
</html>
```